Milo Fenwick - Cinematographer

NEED:
I'm looking for a sleek, professional, modern business card that will give give the recipient the impression that they can trust their production will go smoothly by hiring me. I will bring creativity and knowledge to their shoot, so that we can create powerful images.
I am looking for a card with a strong style and design ethos that could be expanded to a website and a full visual/graphic/design entity for me.
ABOUT ME:
I am a mid-twenties cinematographer, I work on music video, narrative short, commercial, and corporate projects. I blend the science and artistry of cameras and filmmaking to tell a story. I'm an artist, a technician, and a manager.
DESIGN:
I like sleek, simple design. Black, dark grays, white, dark navy, steel blues, I love cyan, but also cyan and red. I am not a fan of earthy tones. I generally prefer modern, san-serif fonts over serifs. My old logo was based on an aperture, a multi-blade device at the back of a lens that controls how much light passes through, but I made it with so many colors, that it doesn't necessarily lend itself to a specific color-scheme or design ethos. I liked that the aperture design provided a sense of the technical requirements of my job. I'm a fan of matte business cards, but am open to plenty of specialty print processes to make an outstanding card.
ATTACHED FILES:
My Old Rainbox Aperture Logo, plus a few designs I've tried playing around with, but am not tied to. I AM OPEN TO NEW DESIGNS, DO NOT FEEL TIED TO THIS.
**I've pulled my old logo down from the attached files, and instead attached other business cards I like, so as not to mislead you where I would like to go.
INFO:
Name: Milo Fenwick
Job: Cinematographer
Email: mpfenwick@quellbox.net
Phone: 415.555.0193
Website: milofenwick.net
I'm adding some images of other cards that I like, and removing my old logo, since I'm looking for something new, and don't want that old logo to push anyone a certain direction.

```html
<!DOCTYPE html>
<html lang="en">
<head>
<meta charset="utf-8">
<title>Milo Fenwick – Cinematographer Business Card</title>
<link rel="stylesheet" href="https://fonts.googleapis.com/css2?family=Open+Sans:wght@300;400;700&family=Source+Code+Pro:wght@400;700&display=swap">
<style>
  :root {
    --backdrop: #6d6d6d;
    --front-card: #1b1d1f;
    --front-ink: #ffffff;
    --back-card: #c3c5c6;
    --back-ink: #1e1f20;
  }
  html, body {
    margin: 0;
    width: 1200px;
    height: 1200px;
    overflow: hidden;
    background: var(--backdrop);
  }
  .presentation { display: block; width: 1200px; height: 1200px; }

  .front .guide, .front .name-frame, .front .rule { stroke: var(--front-ink); fill: none; }
  .front .name-frame { fill: var(--front-card); }
  .front .arrowhead, .front .label { fill: var(--front-ink); }

  .back .card-face { fill: var(--back-card); }
  .back .guide, .back .name-frame { stroke: var(--back-ink); fill: none; }
  .back .name-frame { fill: var(--back-card); }
  .back .arrowhead, .back .label { fill: var(--back-ink); }

  .guide { stroke-width: 2.4; }
  .name-frame { stroke-width: 2.8; }
  .rule { stroke-width: 1.6; }

  .name-first { font-family: "Open Sans", sans-serif; font-weight: 300; font-size: 30px; letter-spacing: 1px; }
  .name-last { font-family: "Open Sans", sans-serif; font-weight: 700; font-size: 31px; letter-spacing: 0.3px; }
  .role-title { font-family: "Open Sans", sans-serif; font-weight: 400; font-size: 32px; }
  .contact { font-family: "Source Code Pro", monospace; font-size: 15px; }
  .contact-name { font-weight: 700; }
</style>
</head>
<body>
<svg class="presentation" viewBox="0 0 1200 1200" xmlns="http://www.w3.org/2000/svg">
  <defs>
    <linearGradient id="front-shade" x1="0" y1="0" x2="0" y2="1">
      <stop offset="0" stop-color="#1f2123"/>
      <stop offset="1" stop-color="#141617"/>
    </linearGradient>

    <symbol id="card-front" viewBox="0 0 738 421" class="front">
      <rect class="card-face" width="738" height="421" fill="url(#front-shade)"/>
      <line class="guide" x1="150" y1="0" x2="150" y2="421"/>
      <line class="guide" x1="0" y1="153" x2="738" y2="153"/>
      <polygon class="arrowhead" points="150,44 145,55 155,55"/>
      <polygon class="arrowhead" points="150,345 145,334 155,334"/>
      <polygon class="arrowhead" points="22,153 33,148 33,158"/>
      <polygon class="arrowhead" points="404,153 393,148 393,158"/>
      <rect class="name-frame" x="64" y="100" width="178" height="104" rx="8"/>
      <text class="label name-first" x="153" y="146" text-anchor="middle">MILO</text>
      <text class="label name-last" x="153" y="186" text-anchor="middle">FENWICK</text>

      <text class="label role-title" x="228" y="263" textLength="478" lengthAdjust="spacingAndGlyphs">CINEMATOGRAPHER</text>

      <line class="rule" x1="472" y1="292" x2="472" y2="373"/>
      <text class="label contact contact-name" x="484" y="305">Milo Fenwick</text>
      <text class="label contact" x="484" y="327">Phone: 415.555.0193</text>
      <text class="label contact" x="484" y="349" textLength="240" lengthAdjust="spacingAndGlyphs">mail :mpfenwick@quellbox.net</text>
      <text class="label contact" x="484" y="371">(www.milofenwick.net)</text>
    </symbol>

    <symbol id="card-back" viewBox="0 0 738 421" class="back">
      <rect class="card-face" width="738" height="421"/>
      <line class="guide" x1="367" y1="0" x2="367" y2="421"/>
      <line class="guide" x1="0" y1="208" x2="738" y2="208"/>
      <polygon class="arrowhead" points="367,44 362,55 372,55"/>
      <polygon class="arrowhead" points="367,345 362,334 372,334"/>
      <polygon class="arrowhead" points="118,208 129,203 129,213"/>
      <polygon class="arrowhead" points="603,208 592,203 592,213"/>
      <rect class="name-frame" x="278" y="156" width="178" height="104" rx="8"/>
      <text class="label name-first" x="367" y="202" text-anchor="middle">MILO</text>
      <text class="label name-last" x="367" y="242" text-anchor="middle">FENWICK</text>
    </symbol>
  </defs>

  <g class="card-pair-large">
    <use href="#card-back" x="401" y="362" width="739" height="422"/>
    <use href="#card-front" x="78" y="68" width="738" height="421"/>
  </g>
  <g class="card-pair-small">
    <use href="#card-front" x="136" y="900" width="424" height="242"/>
    <use href="#card-back" x="648" y="900" width="424" height="242"/>
  </g>
</svg>
</body>
</html>
```